"contact us" Flyer for Marketing Drop-offs

We need a simple 3rd of a page (3 3/4" x 8 1/2") flyer made for quick customer interaction.

These should display our logo, tagline, and our contact information. The background should incorporate the attached picture/color scheme.

This flyer will be offering an incentive to be determined at a later date.

Industry/Entity Type

Legal

Font styles to use
Serif
Sans Serif

Colors
0255a3
33a6d7
876aae

Requirements
Must have
• proper color scheme, simple/modern layout, attached logo
Nice to have
• creativity with working, placement
Should not have
• extra/meaningless characters, shapes

```html
<!DOCTYPE html>
<html lang="en">
<head>
<meta charset="utf-8">
<title>Prairie Ledger – Contact Flyer</title>
<link href="https://fonts.googleapis.com/css2?family=Raleway:wght@500;600;700;800&display=swap" rel="stylesheet">
<style>
  :root {
    --brand-blue: #0255a3;
    --sky-blue: #33a6d7;
    --navy: #2a3a5e;
    --map-grey: #767676;
    --page-bg: #e4e4e4;
    --white: #ffffff;
  }
  * { box-sizing: border-box; margin: 0; padding: 0; }
  html, body { width: 1200px; height: 1200px; overflow: hidden; }
  body {
    background: var(--page-bg);
    font-family: 'Raleway', Arial, sans-serif;
    position: relative;
  }
  .flyer {
    position: absolute;
    left: 58px; top: 362px;
    width: 1080px; height: 478px;
    background: var(--white);
  }
  .band-top {
    position: absolute; left: 0; top: 0;
    width: 364px; height: 37px;
    background: var(--brand-blue);
  }
  .band-right {
    position: absolute; left: 978px; top: 0;
    width: 102px; height: 478px;
    background: var(--brand-blue);
  }
  .band-bottom {
    position: absolute; left: 0; top: 440px;
    width: 1080px; height: 38px;
    background: var(--brand-blue);
  }
  .tagline-box {
    position: absolute; left: 365px; top: 38px;
    width: 715px; height: 126px;
    background: var(--sky-blue);
    padding: 14px 34px 0 30px;
  }
  .tagline {
    color: var(--white);
    font-weight: 700;
    font-size: 26.5px;
    line-height: 34px;
    text-align: justify;
  }
  .brand {
    position: absolute; left: 30px; top: 91px;
    width: 300px;
    text-align: center;
  }
  .brand-map {
    display: block;
    width: 244px; height: 190px;
    margin: 0 auto;
    background: linear-gradient(135deg, var(--map-grey), #5b6480);
    border-radius: 6px;
  }
  .brand-name {
    margin-top: 24px;
    color: var(--navy);
    font-weight: 800;
    font-size: 36px;
    line-height: 40px;
  }
  .brand-sub {
    margin-top: 6px;
    color: var(--navy);
    font-weight: 700;
    font-size: 19px;
  }
  .contacts {
    position: absolute; left: 400px; top: 194px;
    list-style: none;
  }
  .contact {
    display: flex; align-items: center;
    height: 43px;
    margin-bottom: 15px;
    color: var(--brand-blue);
    font-weight: 600;
    font-size: 26px;
  }
  .contact-icon {
    width: 43px; height: 43px;
    border-radius: 50%;
    background: var(--brand-blue);
    display: flex; align-items: center; justify-content: center;
    margin-right: 16px;
    flex-shrink: 0;
  }
  .contact-icon svg { width: 24px; height: 24px; }
</style>
</head>
<body>
  <main class="flyer">
    <div class="band-top"></div>
    <div class="band-right"></div>
    <div class="band-bottom"></div>

    <section class="tagline-box">
      <p class="tagline">Prairie Ledger is the premier source of Country Clerk Records and Mineral Appraisal Data covering Texas, Oklahoma, New Mexico and Colorado.</p>
    </section>

    <section class="brand">
      <div class="brand-map" role="img" aria-label="State map illustration with grid of data tiles"></div>
      <div class="brand-name">Prairie Ledger</div>
      <div class="brand-sub">Land &amp; Mineral Data</div>
    </section>

    <ul class="contacts">
      <li class="contact">
        <span class="contact-icon">
          <svg viewBox="0 0 24 24" fill="none" stroke="#fff" stroke-width="2"><path d="M12 21s-6-6.5-6-11a6 6 0 0 1 12 0c0 4.5-6 11-6 11z"/><circle cx="12" cy="10" r="2.2"/></svg>
        </span>
        42 Harbor Lane, Midtown
      </li>
      <li class="contact">
        <span class="contact-icon">
          <svg viewBox="0 0 24 24" fill="none" stroke="#fff" stroke-width="2"><rect x="7" y="2.5" width="10" height="19" rx="2"/><line x1="11" y1="18" x2="13" y2="18"/></svg>
        </span>
        +1 555 014 2290
      </li>
      <li class="contact">
        <span class="contact-icon">
          <svg viewBox="0 0 24 24" fill="#fff"><path d="M3 9l9-5 9 5v10H3z"/><path d="M3 9l9 6 9-6" fill="none" stroke="#0255a3" stroke-width="1.6"/></svg>
        </span>
        hello@prairieledger.com
      </li>
      <li class="contact">
        <span class="contact-icon">
          <svg viewBox="0 0 24 24" fill="none" stroke="#fff" stroke-width="1.6"><circle cx="12" cy="12" r="9"/><ellipse cx="12" cy="12" rx="4" ry="9"/><line x1="3" y1="12" x2="21" y2="12"/><line x1="4.5" y1="7.5" x2="19.5" y2="7.5"/><line x1="4.5" y1="16.5" x2="19.5" y2="16.5"/></svg>
        </span>
        prairieledger.com
      </li>
    </ul>
  </main>
</body>
</html>
```